MOSLEN Environmental needs an upgrade to its current business cards design

We need an upgrade to our current business cards design, where the MOSLEN acronym is included, as possible and not being overloaded.
MOSLEN Environmental is an Environmental Consultancy Firm based in Sydney.
We would like to see creative designs different from the standard type of business cards (for example, rounded edges, different to standard size of common business cards.

Target Market(s)

industrial companies (oil & gas, petrochemical, mining, insolvency, finance and manufacturing), developers, architect firms, law firms.

Industry/Entity Type

Business

Contact Information for Business Card

logos (brand and acronym), if they don't appear overloaded.
name
role
name of company (MOSLEN Environmental),
address (Level 3, Suite 3C, 47-49 Dorrigan Lane, Wexmoor, NSW, 2188) landline (02 7314 2986)
mobile (staff member)
email (staff member) and
website (www.moslengreen.example).
Include: Contaminated Land, Site Remediation, Groundwater Assessment, Health and Ecological Risk Assessments, Acid Sulfate Soils, Waste Classification.

Font styles to use
Serif
Sans Serif

Requirements
Must have
• A creative design different to the standard type of business cards.
Nice to have
• Rounded edges
• Different size of business cards rather than the standard size.
Should not have
• Preferable not to use white colour background, unless it is required from a creative design proposed.
• Not an overloaded design.
• Avoid black colours

```html
<!DOCTYPE html>
<html lang="en">
<head>
<meta charset="utf-8">
<title>MOSLEN Environmental – Business Cards</title>
<link rel="stylesheet" href="https://fonts.googleapis.com/css2?family=Open+Sans:wght@400;600;700&family=Arimo:wght@700&display=swap">
<style>
  :root {
    --bg: #e9e7e4;
    --card-front: #ffffff;
    --card-back: #1f1d1d;
    --green: #6a9e22;
    --green-dot: #7cb42c;
    --grey-text: #555555;
    --ink: #2b2b2b;
    --white: #ffffff;
  }
  * { margin: 0; padding: 0; box-sizing: border-box; }
  html, body { width: 1200px; height: 900px; overflow: hidden; background: var(--bg); }
  .canvas { position: relative; width: 1200px; height: 900px; }

  .card { position: absolute; border-radius: 18px; box-shadow: 0 4px 14px rgba(0,0,0,.12); }
  .card--front { left: 78px; top: 34px; width: 588px; height: 364px; background: var(--card-front); }
  .card--back { left: 389px; top: 505px; width: 566px; height: 350px; background: var(--card-back); }

  /* acronym column */
  .acronym { position: absolute; left: 50px; top: 56px; list-style: none; }
  .acronym__row { display: flex; align-items: center; height: 44px; }
  .acronym__letter {
    width: 47px; text-align: center;
    font-family: "Open Sans", sans-serif; font-weight: 700; font-size: 44px; line-height: 1;
    color: var(--green);
  }
  .acronym__word {
    margin-left: 0; font-family: "Arimo", sans-serif; font-weight: 700; font-size: 15.5px;
    color: var(--grey-text); letter-spacing: .2px;
  }

  /* contact block */
  .contact { position: absolute; left: 282px; top: 66px; font-family: "Open Sans", sans-serif; color: var(--ink); }
  .contact__name { font-size: 21px; font-weight: 600; color: var(--green); line-height: 1.1; }
  .contact__role { font-size: 15.5px; line-height: 1.3; }
  .contact__list { list-style: none; margin-top: 20px; }
  .contact__item { display: flex; align-items: center; font-size: 15.5px; line-height: 21px; }
  .contact__icon { width: 12px; height: 12px; margin-right: 9px; flex: none; }
  .contact__company { margin-top: 14px; font-size: 15.5px; font-weight: 700; line-height: 1.3; }
  .contact__address { font-size: 15.5px; line-height: 21px; }

  /* back */
  .brand { position: absolute; left: 0; right: 0; top: 118px; text-align: center; font-family: "Open Sans", sans-serif; font-weight: 700; color: var(--green); }
  .brand__name { font-size: 60px; line-height: 1; letter-spacing: 1px; }
  .brand__sub { font-size: 19px; letter-spacing: 2.5px; margin-top: 4px; }
  .services { position: absolute; left: 0; right: 0; top: 242px; text-align: center; font-family: "Open Sans", sans-serif; font-size: 15.5px; line-height: 21px; color: var(--white); }
  .services__dot { display: inline-block; width: 9px; height: 9px; border-radius: 50%; background: var(--green-dot); margin: 0 7px; vertical-align: 1px; }
</style>
</head>
<body>
<main class="canvas">

  <section class="card card--front" aria-label="Business card front">
    <ul class="acronym">
      <li class="acronym__row"><span class="acronym__letter">M</span><span class="acronym__word">ONITORING</span></li>
      <li class="acronym__row"><span class="acronym__letter">O</span><span class="acronym__word">VERSIGHT (AND)</span></li>
      <li class="acronym__row"><span class="acronym__letter">S</span><span class="acronym__word">URVEYS (OF)</span></li>
      <li class="acronym__row"><span class="acronym__letter">L</span><span class="acronym__word">AND</span></li>
      <li class="acronym__row"><span class="acronym__letter">E</span><span class="acronym__word">COLOGY (AND)</span></li>
      <li class="acronym__row"><span class="acronym__letter">N</span><span class="acronym__word">ATURAL SYSTEMS</span></li>
    </ul>

    <div class="contact">
      <p class="contact__name">Daniel Harper</p>
      <p class="contact__role">Managing Director</p>
      <ul class="contact__list">
        <li class="contact__item">
          <svg class="contact__icon" viewBox="0 0 12 12"><rect x="3" y="0.5" width="6" height="11" rx="1.2" fill="none" stroke="var(--green)" stroke-width="1.4"/><circle cx="6" cy="9.5" r=".8" fill="var(--green)"/></svg>
          0491 572 630
        </li>
        <li class="contact__item">
          <svg class="contact__icon" viewBox="0 0 12 12"><path d="M2.2 .8 4.4 3 3.3 4.4c.8 1.7 2.2 3.1 4.3 4.3L9 7.6l2.2 2.2-1.5 1.6C5.3 11 1 6.7.6 2.3z" fill="var(--green)"/></svg>
          02 7314 2986
        </li>
        <li class="contact__item">
          <svg class="contact__icon" viewBox="0 0 12 12"><rect x="0.5" y="2" width="11" height="8" fill="var(--green)"/><path d="M.8 2.4 6 6.6l5.2-4.2" fill="none" stroke="#fff" stroke-width="1.1"/></svg>
          info@moslengreen.example
        </li>
        <li class="contact__item">
          <svg class="contact__icon" viewBox="0 0 12 12"><circle cx="6" cy="6" r="5.5" fill="var(--green)"/><path d="M3 4.5c1 0 1.5.8 2.4 1.6.5.5 0 1.4.5 2.4M7.5 1.5c-.5 1.2.6 1.5 1.3 2.2.6.6 1.4.4 2.2.4" fill="none" stroke="#fff" stroke-width=".9"/></svg>
          www.moslengreen.example
        </li>
      </ul>
      <p class="contact__company">MOSLEN Environmental</p>
      <p class="contact__address">Level 3, Suite 3C, 47-49 Dorrigan Lane,<br>Wexmoor, NSW, 2188</p>
    </div>
  </section>

  <section class="card card--back" aria-label="Business card back">
    <div class="brand">
      <p class="brand__name">MOSLEN</p>
      <p class="brand__sub">ENVIRONMENTAL</p>
    </div>
    <p class="services">
      Contaminated Land<span class="services__dot"></span>Site Remediation<span class="services__dot"></span>Groundwater Assessment<br>
      Health and Ecological Risk Assessments<span class="services__dot"></span>Acid Sulfate Soils<br>
      <span class="services__dot"></span>Waste Classification.
    </p>
  </section>

</main>
</body>
</html>
```